Name Card Design - CuiFeng Enterprise Pte Ltd

Family office operations base in Singapore that deals with financial investments and trading. Company name is direct english translation of Chinese characters 翠枫 (meaning overflowing/surplus + stable as mountain)。We do not have a company logo design yet. Was considering having the logo as traditional chinese seal design. Other ideas are welcomed.

Target Market(s)

financial institutions, investors, networking

Industry/Entity Type

Finance

Contact Information for Business Card

Pls use fictitious names and contact details in design

Requirements
Must have
• Logo, Name, Title, Address, Email, Tel, Mobile

```html
<!DOCTYPE html>
<html lang="en">
<head>
<meta charset="utf-8">
<title>CuiFeng Enterprise Pte Ltd – Name Card</title>
<link rel="stylesheet" href="https://fonts.googleapis.com/css2?family=Encode+Sans+Semi+Condensed:wght@400;600&family=Pathway+Gothic+One&display=swap">
<style>
  :root {
    --page: #ffffff;
    --card: #ffffff;
    --card-edge: #cfcfcf;
    --ink: #111111;
    --accent: #a11d1d;
  }
  html, body {
    margin: 0;
    width: 1200px;
    height: 899px;
    overflow: hidden;
    background: var(--page);
  }
  .card {
    position: absolute;
    left: 275px;
    top: 264px;
    width: 649px;
    height: 370px;
    background: var(--card);
    border: 1px solid var(--card-edge);
    font-family: "Encode Sans Semi Condensed", sans-serif;
    color: var(--ink);
  }
  .brand-mark {
    position: absolute;
    left: 46px;
    top: 46px;
    width: 57px;
    height: 57px;
    background: var(--accent);
    border-radius: 3px;
  }
  .company {
    position: absolute;
    left: 118px;
    top: 60px;
    margin: 0;
    font-size: 33px;
    font-weight: 400;
    font-variant: small-caps;
    letter-spacing: 0.3px;
    line-height: 1;
  }
  .person {
    position: absolute;
    left: 118px;
    top: 164px;
  }
  .person-name {
    margin: 0;
    font-size: 28px;
    font-weight: 400;
    font-variant: small-caps;
    line-height: 1;
  }
  .person-name .surname { font-weight: 600; }
  .person-title {
    margin: 4px 0 0;
    font-size: 22px;
    line-height: 1;
    letter-spacing: 0.3px;
  }
  .contacts {
    position: absolute;
    left: 315px;
    top: 238px;
    margin: 0;
    padding: 0;
    list-style: none;
    font-family: "Pathway Gothic One", sans-serif;
    font-size: 24px;
    line-height: 30px;
  }
  .contacts li {
    display: flex;
    align-items: center;
    gap: 8px;
  }
  .contact-icon {
    width: 21px;
    height: 21px;
    flex: none;
  }
</style>
</head>
<body>
  <div class="card">
    <div class="brand-mark" aria-hidden="true"></div>
    <h1 class="company">CuiFeng Enterprise Pte Ltd</h1>

    <div class="person">
      <p class="person-name"><span class="surname">Lim</span> Wei Jie</p>
      <p class="person-title">DIRECTOR</p>
    </div>

    <ul class="contacts">
      <li>
        <svg class="contact-icon" viewBox="0 0 21 21" aria-hidden="true">
          <rect width="21" height="21" rx="5" fill="var(--accent)"/>
          <path d="M10.5 3.5a5 5 0 0 0-5 5c0 3.6 5 9 5 9s5-5.4 5-9a5 5 0 0 0-5-5z" fill="#fff"/>
          <circle cx="10.5" cy="8.5" r="2" fill="var(--accent)"/>
        </svg>
        <span>18B Maple Lane Singapore 529117</span>
      </li>
      <li>
        <svg class="contact-icon" viewBox="0 0 21 21" aria-hidden="true">
          <rect width="21" height="21" rx="5" fill="var(--accent)"/>
          <path d="M6 4.5l2.4-.3 1.3 3-1.5 1.2a8 8 0 0 0 3.6 3.6l1.2-1.5 3 1.3-.3 2.4c-.1.6-.7 1-1.3 1C9 15 6 12 5 6.8c0-.6.4-1.2 1-1.3z" fill="#fff"/>
        </svg>
        <span>+65 8246 1730</span>
      </li>
      <li>
        <svg class="contact-icon" viewBox="0 0 21 21" aria-hidden="true">
          <rect width="21" height="21" rx="5" fill="var(--accent)"/>
          <rect x="4" y="6" width="13" height="9" fill="none" stroke="#fff" stroke-width="1.5"/>
          <path d="M4 6l6.5 5 6.5-5M4 15l5-4.5M17 15l-5-4.5" fill="none" stroke="#fff" stroke-width="1.2"/>
        </svg>
        <span>wjlim@cuifeng.com.sg</span>
      </li>
    </ul>
  </div>
</body>
</html>
```